KVR Associates needs a web site

We need a web site for www.kvrassociates-example.com. KVR is a mergers and acquisition consulting company that focuses our buyer and seller services on logistics companies. We help put companies together, and help with legal and financial due diligence. We want the web site to express our service and show the logistics components. We want personalized images versus pictures of trucks and airplanes.

Our new logo uses Burgandy and grey colors. Image attached. We are not in to bold, big letters...classy, artistic, low key preferred. Confidentiality, experience, professional are what we want to express on the site.

All we expect for the first part of this project is a home page, and one subpage.  We are budgeting other funds for the technical aspects of the web site

Reason: All that I'm seeing so far is trucks, forklifts and planes. We are a legal mergers and acquisitions firm that focus on logistics. I like some of the images to say logistics, but really want it say legal, financial, and putting companies together. Will pay extra for the sub page if someone can impress us with a home page.

Reason: Swamped with another project at the moment...will work on this over the weekend and provide designer feedback and select final design by Tuesday

```html
<!DOCTYPE html>
<html lang="en">
<head>
<meta charset="utf-8">
<title>KVR Associates — Home</title>
<link rel="stylesheet" href="https://fonts.googleapis.com/css2?family=Arimo:ital,wght@0,400;0,700;1,400&family=Roboto+Condensed:wght@300;400;700&family=PT+Sans:wght@400;700&display=swap">
<style>
  :root {
    --crimson: #a50034;
    --ink: #1c1c1c;
    --charcoal: #262626;
    --text: #222222;
    --field: #d9d9d9;
    --taupe: #d3cdc7;
    --social: #3d6ea8;
    --white: #ffffff;
  }
  * { box-sizing: border-box; margin: 0; padding: 0; }
  html, body { width: 876px; height: 1200px; overflow: hidden; background: var(--white); }
  body { font-family: "Arimo", Arial, sans-serif; color: var(--text); }
  .page { position: relative; width: 876px; height: 1200px; overflow: hidden; }
  .abs { position: absolute; }

  /* Top navigation */
  .topnav { left: 0; top: 0; width: 876px; height: 44px; background: var(--ink); }
  .topnav a, .footnav a {
    position: absolute; text-decoration: none; text-transform: uppercase; white-space: nowrap;
  }
  .topnav a { top: 17px; color: var(--white); font-size: 8px; }
  .topnav .active { left: 175px; top: 0; width: 52px; height: 44px; background: var(--crimson); text-align: center; line-height: 44px; }

  /* Hero */
  .hero { left: 0; top: 44px; width: 876px; height: 416px; }
  .hero-photo { position: absolute; inset: 0;
    background: linear-gradient(180deg, #a9b6c1 0%, #b9c0c4 30%, #6f7569 55%, #545a56 75%, #74777c 100%); }
  .brand-band { position: absolute; left: 0; top: 0; width: 876px; height: 84px; background: rgba(255,255,255,.55); }
  .brand { position: absolute; left: 118px; top: 22px; display: flex; align-items: center; gap: 12px; }
  .brand-mark { width: 30px; height: 30px; background: var(--crimson); }
  .brand-name { font-family: "Roboto Condensed", sans-serif; font-weight: 400; font-size: 36px; color: #4a4a4a; letter-spacing: 1px; }
  .search { position: absolute; left: 640px; top: 16px; width: 100px; height: 22px; background: var(--white);
    font-size: 8.5px; color: #a0a0a0; padding: 6px 6px; letter-spacing: .5px; }
  .search-btn { position: absolute; left: 740px; top: 16px; width: 24px; height: 22px; background: var(--crimson); }
  .headline { position: absolute; left: 245px; top: 266px; width: 406px; height: 76px; background: rgba(30,30,30,.78);
    color: var(--white); font-size: 30px; line-height: 35px; text-align: center; padding-top: 4px; text-transform: uppercase; }
  .caption { position: absolute; left: 186px; top: 350px; width: 504px; height: 43px; background: var(--crimson);
    color: var(--white); font-size: 11px; line-height: 16px; text-align: center; padding: 5px 24px 0; }
  .slide-arrow { position: absolute; top: 358px; width: 38px; height: 26px; background: #161616; }

  /* Welcome */
  .welcome-title { left: 130px; top: 481px; font-family: "Roboto Condensed", sans-serif; font-weight: 300;
    font-size: 28px; color: var(--crimson); text-transform: uppercase; }
  .welcome-title strong { font-weight: 700; }
  .welcome-copy { left: 130px; top: 522px; width: 618px; font-size: 9.6px; line-height: 14px; color: var(--text); }

  /* Services */
  .services { left: 0; top: 590px; width: 876px; height: 286px; background: var(--crimson); }
  .services-title { left: 130px; top: 19px; font-family: "Roboto Condensed", sans-serif; font-weight: 300; font-size: 27px; color: var(--white); }
  .service { position: absolute; top: 66px; width: 199px; }
  .service-photo { position: relative; width: 199px; height: 102px; }
  .service-label { position: absolute; left: 0; bottom: 0; width: 142px; height: 25px; background: rgba(25,25,25,.85);
    color: var(--white); font-size: 14.5px; line-height: 25px; padding-left: 12px; }
  .service-copy { margin-top: 13px; font-size: 8px; line-height: 13px; color: var(--white); text-align: justify; }
  .service-more { margin-top: 13px; font-size: 8px; color: var(--white); letter-spacing: .5px; }

  /* News & newsletter */
  .news-title { left: 130px; top: 904px; font-size: 17px; font-weight: 400; color: var(--ink); }
  .quote-open { left: 150px; top: 940px; font-weight: 700; font-size: 24px; line-height: 1; color: var(--ink); }
  .news-copy { left: 168px; top: 949px; width: 322px; font-size: 8.4px; line-height: 15.4px; color: var(--text); }
  .quote-close { font-weight: 700; font-size: 15px; line-height: 0; color: var(--ink); margin-left: 6px; vertical-align: -3px; }
  .news-more { left: 443px; top: 1022px; font-size: 8.5px; font-style: italic; color: var(--crimson); }
  .divider { left: 534px; top: 898px; width: 1px; height: 156px; background: #cfcfcf; }
  .newsletter-title { left: 582px; top: 915px; font-family: "PT Sans", sans-serif; font-weight: 400; font-size: 18px; color: var(--ink); letter-spacing: .5px; }
  .field { left: 582px; width: 133px; height: 23px; background: var(--field); font-family: "PT Sans", sans-serif;
    font-size: 10.5px; color: #6e6e6e; padding: 5px 6px; }
  .subscribe { left: 582px; top: 1008px; width: 98px; height: 20px; background: var(--crimson); color: var(--white);
    font-family: "PT Sans", sans-serif; font-weight: 700; font-size: 10.5px; line-height: 20px; text-align: center; }

  /* Footer */
  .footnav { left: 0; top: 1062px; width: 876px; height: 42px; background: var(--taupe); }
  .footnav a { top: 18px; color: #333; font-size: 8px; }
  .footnav .active { border-bottom: 1px solid var(--crimson); padding: 0 3px 5px; }
  .footer { left: 0; top: 1104px; width: 876px; height: 96px; background: var(--charcoal); }
  .social { position: absolute; top: 24px; width: 21px; height: 21px; border-radius: 2px; background: var(--social); }
  .copyright { position: absolute; left: 0; width: 876px; top: 63px; text-align: center; color: var(--white); font-size: 7.5px; letter-spacing: .2px; }
</style>
</head>
<body>
<div class="page">

  <nav class="topnav abs">
    <a class="active" href="#">Home</a>
    <a style="left:244px" href="#">About Us</a>
    <a style="left:306px" href="#">Services</a>
    <a style="left:366px" href="#">Request a Quote</a>
    <a style="left:460px" href="#">Office Networks</a>
    <a style="left:559px" href="#">Contact Us</a>
    <a style="left:662px" href="#">General Info</a>
  </nav>

  <header class="hero abs">
    <div class="hero-photo" role="img" aria-label="Photograph of a white articulated lorry on a motorway at sunset"></div>
    <div class="brand-band"></div>
    <div class="brand">
      <span class="brand-mark"></span>
      <span class="brand-name">KVR Associates</span>
    </div>
    <div class="search">SEARCH</div>
    <div class="search-btn">
      <svg width="24" height="22" viewBox="0 0 24 22"><circle cx="10" cy="9" r="4" fill="none" stroke="#fff" stroke-width="1.8"/><line x1="13" y1="12" x2="17" y2="16" stroke="#fff" stroke-width="2.2"/></svg>
    </div>
    <div class="headline">Lorem ipsum dolor sit<br>amet consectetur</div>
    <div class="caption">Lorem ipsum dolor sit amet, consectetur adipisicing elit, sed do eiusmod tempor incididunt ut labore et dolore magna aliqua.</div>
    <div class="slide-arrow" style="left:166px">
      <svg width="38" height="26" viewBox="0 0 38 26"><polyline points="22,7 16,13 22,19" fill="none" stroke="#fff" stroke-width="1.6"/></svg>
    </div>
    <div class="slide-arrow" style="left:673px">
      <svg width="38" height="26" viewBox="0 0 38 26"><polyline points="16,7 22,13 16,19" fill="none" stroke="#fff" stroke-width="1.6"/></svg>
    </div>
  </header>

  <h1 class="welcome-title abs">Welcome to <strong>KVR</strong></h1>
  <p class="welcome-copy abs">KVR assists business owners within the logistics industry to implement growth and exit strategies. We offer business planning and merger and acquisition(M&amp;A) advisory services. KVR services are offered by industry executives with extensive M&amp;A experience.&nbsp; Your company will benefit from a unique and outside perspective from consultants that understand your business.</p>

  <section class="services abs">
    <h2 class="services-title abs">SERVICES</h2>
    <article class="service" style="left:128px">
      <div class="service-photo" role="img" aria-label="Photograph of a container ship at sea" style="background:linear-gradient(180deg,#8a9ea9 0%,#6f8390 100%)">
        <div class="service-label">Lorem ipsum dolor</div>
      </div>
      <p class="service-copy">Lorem ipsum dolor sit amet, consectetur adipisicing elit, sed do eiusmod tempor incididunt ut labore et dolore magna aliqua. Ut enim ad minim veniam, quis nostrud exercitation ullamco laboris</p>
      <p class="service-more">Read More</p>
    </article>
    <article class="service" style="left:340px">
      <div class="service-photo" role="img" aria-label="Photograph of a blue lorry on the road" style="background:linear-gradient(180deg,#cfd7de 0%,#7b93aa 100%)">
        <div class="service-label">Lorem ipsum dolor</div>
      </div>
      <p class="service-copy">Lorem ipsum dolor sit amet, consectetur adipisicing elit, sed do eiusmod tempor incididunt ut labore et dolore magna aliqua. Ut enim ad minim veniam, quis nostrud exercitation ullamco laboris</p>
      <p class="service-more">Read More</p>
    </article>
    <article class="service" style="left:552px">
      <div class="service-photo" role="img" aria-label="Photograph of a passenger jet in flight" style="background:linear-gradient(180deg,#3a6ea8 0%,#8fb0d2 100%)">
        <div class="service-label">Lorem ipsum dolor</div>
      </div>
      <p class="service-copy">Lorem ipsum dolor sit amet, consectetur adipisicing elit, sed do eiusmod tempor incididunt ut labore et dolore magna aliqua. Ut enim ad minim veniam, quis nostrud exercitation ullamco laboris</p>
      <p class="service-more">Read More</p>
    </article>
  </section>

  <h2 class="news-title abs">LATEST NEWS</h2>
  <span class="quote-open abs">&ldquo;</span>
  <p class="news-copy abs">Lorem ipsum dolor sit amet, consectetur adipisicing elit, sed do eiusmod tempor incididunt ut labore et dolore magna aliqua. Ut enim ad minim veniam, quis nostrud exercitation ullamco laboris nisi ut aliquip ex ea commodo consequat. Duis aute irure dolor in reprehenderit in voluptate.<span class="quote-close">&rdquo;</span></p>
  <span class="news-more abs">Read More</span>
  <div class="divider abs"></div>

  <h2 class="newsletter-title abs">NEWSLETTER</h2>
  <div class="field abs" style="top:942px">USERNAME</div>
  <div class="field abs" style="top:973px">USERNAME</div>
  <div class="subscribe abs">SUBSCRIBE NOW</div>

  <nav class="footnav abs">
    <a class="active" style="left:151px" href="#">Home</a>
    <a style="left:209px" href="#">About Us</a>
    <a style="left:284px" href="#">Services</a>
    <a style="left:363px" href="#">Request a Quote</a>
    <a style="left:471px" href="#">Office Networks</a>
    <a style="left:580px" href="#">Contact Us</a>
    <a style="left:667px" href="#">General Info</a>
  </nav>

  <footer class="footer abs">
    <span class="social" style="left:402px"></span>
    <span class="social" style="left:428px"></span>
    <span class="social" style="left:455px"></span>
    <p class="copyright">COPYRIGHT &copy; 2013 / ALL RIGHTS RESERVED.</p>
  </footer>

</div>
</body>
</html>
```